New web design needed for our company

We need our website designing, it needs to be professional and look creative,
We are a plumbing and heating company called Brackwell Flow's (www.brackwellflows.co.uk)
I like this site design also some of the following maybe:
https://www.tindermoorwarmth.com/
http://www.quorvapower.co.uk

Please let me know when you want our logo files as it wont let me upload them

The design will require coding once the design is complete, i havent paid for this yet as i want to be sure the design is good before i commit.

The template needs to look professional and look like one of the leading companies.
The site will consist of all the features this site has https://www.tindermoorwarmth.com/

I like a modern design with the latest technology.

Must have a customer login page and a my account area

Target Market(s)

Everyone

Industry/Entity Type

Plumbing

Coding

Coded - Design and coding required

Number of Pages Required

5+ page

Font styles to use
Other font styles liked:
• whatever suites

Requirements
Must have
• The design will require coding once the design is complete, i havent paid for this yet as i want to be sure the design is good before i commit.
• The template needs to look professional and look like one of the leading companies.
• The site will consist of all the features this site has https://www.tindermoorwarmth.com/
• I like a modern design with the latest technology.
• Must have a customer login page and a my account area
Nice to have
• inspirational and different
Should not have
• plain boring designs like most plumbing websites, needs to be inspiring and attract people from first sight.

```html
<!DOCTYPE html>
<html lang="en">
<head>
<meta charset="utf-8">
<title>Brackwell Flow's – Plumbing and Heating</title>
<link rel="stylesheet" href="https://fonts.googleapis.com/css2?family=Montserrat:wght@500;600;700&family=Open+Sans:wght@400;600&display=swap">
<style>
:root{
  --orange:#f4694f;
  --navy:#10296b;
  --ink:#222;
  --muted:#6b6b6b;
  --line:#e6e6e6;
  --card:#f7f7f7;
  --footer-bar:#ececec;
}
*{box-sizing:border-box;margin:0;padding:0}
html,body{width:676px;height:1200px;overflow:hidden;background:#fff}
body{font-family:"Open Sans",Arial,sans-serif;color:var(--ink);position:relative}
.site-header{position:absolute;top:0;left:0;width:676px;height:53px;background:#fff}
.brand{position:absolute;left:55px;top:12px;font-family:"Montserrat",Arial,sans-serif;font-weight:700;font-size:20px;color:var(--navy);letter-spacing:-.3px}
.brand-tag{position:absolute;left:110px;top:35px;font-size:6px;color:var(--navy)}
.login{position:absolute;left:450px;top:6px;display:flex;align-items:center;gap:6px;font-size:8.5px;color:var(--orange)}
.login .lock{width:19px;height:19px;border-radius:50%;background:var(--orange);display:flex;align-items:center;justify-content:center}
.socials{position:absolute;left:514px;top:6px;display:flex;gap:3px}
.socials span{width:19px;height:19px;border-radius:50%;background:var(--navy)}
.socials span:nth-child(3){background:#333}
.socials span:nth-child(4),.socials span:nth-child(5){background:#d6332b}
.main-nav{position:absolute;left:273px;top:34px;display:flex;gap:18px;font-size:7.8px;color:#333}
.hero{position:absolute;top:53px;left:0;width:676px;height:265px;
  background:
    radial-gradient(ellipse 120px 150px at 600px 70px,rgba(214,40,36,.95),rgba(214,40,36,0) 100%),
    radial-gradient(ellipse 90px 110px at 520px 210px,rgba(120,112,108,.9),rgba(120,112,108,0) 100%),
    radial-gradient(ellipse 70px 60px at 420px 200px,rgba(236,232,226,.9),rgba(236,232,226,0) 100%),
    radial-gradient(ellipse 200px 70px at 180px 30px,rgba(120,110,100,.55),rgba(120,110,100,0) 100%),
    linear-gradient(180deg,#cfcac4 0%,#e4e0db 55%,#b8b1a9 100%)}
.hero-caption{position:absolute;left:36px;top:85px;width:306px;height:85px;background:rgba(40,40,40,.85);padding:17px 19px 0}
.hero-caption h1{font-family:"Montserrat",Arial,sans-serif;font-weight:700;font-size:25px;color:#fff;line-height:1;white-space:nowrap;letter-spacing:.2px}
.hero-caption p{font-family:"Montserrat",Arial,sans-serif;font-weight:500;font-size:10.4px;color:#fff;margin-top:12px;white-space:nowrap}
.hero-arrow{position:absolute;top:115px;width:18px;height:18px;border:1px solid rgba(255,255,255,.8);border-radius:50%}
.hero-arrow svg{display:block;margin:4px auto}
.welcome{position:absolute;top:318px;left:0;width:676px;height:218px}
.video-thumb{position:absolute;left:55px;top:34px;width:272px;height:149px;
  background:
    radial-gradient(ellipse 50px 90px at 20px 90px,rgba(190,45,40,.95),rgba(190,45,40,0) 100%),
    radial-gradient(ellipse 40px 50px at 40px 130px,rgba(40,80,160,.8),rgba(40,80,160,0) 100%),
    radial-gradient(ellipse 80px 60px at 220px 110px,rgba(60,100,175,.9),rgba(60,100,175,0) 100%),
    radial-gradient(ellipse 60px 40px at 180px 30px,rgba(150,170,190,.8),rgba(150,170,190,0) 100%),
    radial-gradient(ellipse 40px 40px at 160px 55px,rgba(230,190,170,.9),rgba(230,190,170,0) 100%),
    linear-gradient(180deg,#e2e3e4,#d4d6d8);box-shadow:0 2px 8px rgba(0,0,0,.25)}
.play{position:absolute;left:122px;top:64px;width:28px;height:19px;border-radius:5px;background:#d8261f}
.welcome-text{position:absolute;left:357px;top:33px;width:264px}
.welcome-text h2{font-family:"Montserrat",Arial,sans-serif;font-weight:700;font-size:15px;color:#111}
.welcome-text p{font-size:6.5px;line-height:11.5px;color:#555;margin-top:10px}
.btns{display:flex;gap:6px;margin-top:16px}
.btn{height:22px;border-radius:11px;font-size:7.5px;color:#fff;display:flex;align-items:center;justify-content:center;font-family:"Montserrat",Arial,sans-serif;font-weight:500}
.btn-orange{width:69px;background:var(--orange)}
.btn-navy{width:62px;background:var(--navy)}
.services{position:absolute;top:536px;left:0;width:676px;height:234px;background:linear-gradient(180deg,rgba(244,105,79,.94),rgba(244,105,79,.9)),#b44;text-align:center;color:#fff}
.services h2{font-family:"Montserrat",Arial,sans-serif;font-weight:700;font-size:16px;margin-top:32px}
.services .lead{font-size:7.8px;margin-top:4px}
.service{position:absolute;top:86px;width:124px;text-align:center}
.ring{width:72px;height:72px;border:2px solid #fff;border-radius:50%;margin:0 auto;display:flex;align-items:center;justify-content:center}
.ring-inner{width:62px;height:62px;border:1px solid rgba(255,255,255,.8);border-radius:50%;display:flex;align-items:center;justify-content:center}
.service h3{font-family:"Open Sans",Arial,sans-serif;font-weight:600;font-size:9px;margin-top:19px}
.service p{font-size:6.2px;margin-top:3px}
.testimonials{position:absolute;top:770px;left:0;width:676px;height:236px;border-bottom:2px solid var(--navy)}
.testimonials h2{font-family:"Montserrat",Arial,sans-serif;font-weight:700;font-size:15.5px;text-align:center;margin-top:32px;color:#111}
.quote-card{position:absolute;top:86px;width:183px;height:72px;background:var(--card);border:1px solid #eee;padding:22px 11px 0;font-size:6.3px;line-height:10.5px;color:#666;text-align:justify}
.quote-card::after{content:"";position:absolute;bottom:-6px;left:88px;border:6px solid transparent;border-bottom:0;border-top-color:var(--card)}
.quote-mark{position:absolute;top:72px;width:30px;height:30px;border-radius:50%;background:var(--navy);display:flex;align-items:center;justify-content:center;color:#fff;font-family:Georgia,serif;font-weight:700;font-size:20px;line-height:1;padding-top:9px}
.client{position:absolute;top:167px;display:flex;align-items:center;gap:10px}
.avatar{width:35px;height:35px;border-radius:50%;border:2px solid var(--orange);background:radial-gradient(circle at 50% 40%,#e0bfa6 0%,#c99e82 35%,#7a5a48 75%,#eee 100%)}
.client-name{font-size:8.5px;color:#333}
.stars{font-size:7px;color:#e8a33a;letter-spacing:1px;margin-top:1px}
.site-footer{position:absolute;top:1008px;left:0;width:676px;height:160px}
.foot-col{position:absolute;top:28px}
.foot-col h4{font-family:"Montserrat",Arial,sans-serif;font-weight:500;font-size:9.2px;color:#222;letter-spacing:.3px}
.foot-col ul{list-style:none;margin-top:10px}
.foot-col li{font-size:6.4px;color:#555;height:17px}
.contact li{display:flex;gap:7px;line-height:12px;height:auto;margin-bottom:5px}
.contact li.nowrap{white-space:nowrap}
.contact svg{flex:none;margin-top:2px}
.bottom-bar{position:absolute;top:1168px;left:0;width:676px;height:32px;background:var(--footer-bar);font-size:6.6px;color:#333;text-align:center;line-height:32px}
</style>
</head>
<body>
<header class="site-header">
  <div class="brand">Brackwell Flow's</div>
  <div class="brand-tag">Your Local Experts</div>
  <div class="login"><span class="lock"><svg width="8" height="9" viewBox="0 0 8 9"><rect x="0.5" y="4" width="7" height="5" fill="#fff"/><path d="M2 4V2.6a2 2 0 0 1 4 0V4" stroke="#fff" fill="none" stroke-width="1.2"/></svg></span>LOGIN</div>
  <div class="socials"><span></span><span></span><span></span><span></span><span></span></div>
  <nav class="main-nav"><span>Home</span><span>Services</span><span>Emergencies</span><span>BusinessCustomers</span><span>Pro Care</span><span>Help &amp; Support</span></nav>
</header>

<section class="hero" role="img" aria-label="Plumber in a red shirt fitting pipework under a sink">
  <div class="hero-arrow" style="left:10px"><svg width="8" height="8" viewBox="0 0 8 8"><path d="M5 1L2 4l3 3" stroke="#fff" fill="none"/></svg></div>
  <div class="hero-arrow" style="right:12px"><svg width="8" height="8" viewBox="0 0 8 8"><path d="M3 1l3 3-3 3" stroke="#fff" fill="none"/></svg></div>
  <div class="hero-caption">
    <h1>BRACKWELL FLOW'S</h1>
    <p>WE ARE A PLUMBING AND HEATING COMPANY.</p>
  </div>
</section>

<section class="welcome">
  <div class="video-thumb" role="img" aria-label="Video still of an engineer adjusting a boiler control panel">
    <div class="play"><svg width="28" height="19" viewBox="0 0 28 19"><path d="M11 5l7 4.5-7 4.5z" fill="#fff"/></svg></div>
  </div>
  <div class="welcome-text">
    <h2>WELCOME TO OUR COMPANY</h2>
    <p>Lorem Ipsum is simply dummy text of the printing and typesetting industry. Lorem Ipsum has been the industry's standard dummy text ever since the 1500s, when an unknown printer took a galley of type and scrambled it to make a type specimen book. It has survived not only five centuries</p>
    <p>Lorem Ipsum is simply dummy text of the printing and typesetting industry. Lorem Ipsum has been the industry's standard dummy text ever since the 1500s, when an unknown printer took a galley of type and scrambled</p>
    <div class="btns"><span class="btn btn-orange">CONTACT US</span><span class="btn btn-navy">READ MORE</span></div>
  </div>
</section>

<section class="services">
  <h2>OUR SERVICES</h2>
  <p class="lead">No project is ever too large or too small, and there's nearly</p>
  <div class="service" style="left:30px">
    <div class="ring"><div class="ring-inner"><svg width="34" height="24" viewBox="0 0 34 24" fill="#fff"><path d="M1 6l8-4 8 5 8-5 8 4v9l-6 3-10 5-4-3-4-3-8-3z"/></svg></div></div>
    <h3>Business services</h3><p>To learn more about services</p>
  </div>
  <div class="service" style="left:153px">
    <div class="ring"><div class="ring-inner"><svg width="28" height="28" viewBox="0 0 28 28" fill="#fff"><path d="M4 3a6 6 0 0 0 7 8l12 12a2.5 2.5 0 0 0 3.5-3.5L14.5 7.5A6 6 0 0 0 6.5 1L10 4.5 9 8 5.5 9z"/></svg></div></div>
    <h3>Plumbing</h3><p>To learn more about services</p>
  </div>
  <div class="service" style="left:276px">
    <div class="ring"><div class="ring-inner"><svg width="22" height="30" viewBox="0 0 22 30"><path d="M11 1c1 6 10 9 10 18a10 10 0 0 1-20 0c0-5 3-7 4-10 1 3 2 4 3 4-1-4 1-8 3-12z" fill="#fff"/><path d="M11 14c2 3 5 5 5 9a5 5 0 0 1-10 0c0-3 3-5 5-9z" fill="#f4694f"/></svg></div></div>
    <h3>Heating</h3><p>To learn more about services</p>
  </div>
  <div class="service" style="left:399px">
    <div class="ring"><div class="ring-inner"><svg width="30" height="26" viewBox="0 0 30 26" fill="#fff"><path d="M15 1L1 13h4v12h8v-8h4v8h8V13h4z"/></svg></div></div>
    <h3>Landlord services</h3><p>To learn more about services</p>
  </div>
  <div class="service" style="left:522px">
    <div class="ring"><div class="ring-inner"><svg width="32" height="28" viewBox="0 0 32 28" fill="none" stroke="#fff" stroke-width="2"><path d="M2 12L16 2l14 10"/><path d="M9 17l4-3 3 2 3-2 4 3-5 3h-4z" fill="#fff" stroke="none"/><path d="M3 25h26"/></svg></div></div>
    <h3>Estate Agents</h3><p>To learn more about services</p>
  </div>
</section>

<section class="testimonials">
  <h2>OUR CLIENT TESTIMONIAL</h2>
  <div class="quote-card" style="left:55px">" There are many variations of passages of Lorem Ipsum available, but the majority have suffered alteration in some form, by injected humour, or randomised words which don't look"</div>
  <div class="quote-card" style="left:247px">" There are many variations of passages of Lorem Ipsum available, but the majority have suffered alteration in some form, by injected humour, or randomised words which don't look"</div>
  <div class="quote-card" style="left:438px">" There are many variations of passages of Lorem Ipsum available, but the majority have suffered alteration in some form, by injected humour, or randomised words which don't look"</div>
  <div class="quote-mark" style="left:132px">"</div>
  <div class="quote-mark" style="left:323px">"</div>
  <div class="quote-mark" style="left:514px">"</div>
  <div class="client" style="left:57px"><div class="avatar" role="img" aria-label="Client portrait"></div><div><div class="client-name">Darren P. Holloway-WA</div><div class="stars">☆☆☆☆☆</div></div></div>
  <div class="client" style="left:249px"><div class="avatar" role="img" aria-label="Client portrait"></div><div><div class="client-name">Maribel T.</div><div class="stars">☆☆☆☆☆</div></div></div>
  <div class="client" style="left:440px"><div class="avatar" role="img" aria-label="Client portrait"></div><div><div class="client-name">Lorna K. Kentfield-WA</div><div class="stars">☆☆☆☆☆</div></div></div>
</section>

<footer class="site-footer">
  <div class="foot-col contact" style="left:55px;width:120px">
    <h4>CONTACT US</h4>
    <ul>
      <li><svg width="6" height="8" viewBox="0 0 6 8"><path d="M3 0a3 3 0 0 1 3 3c0 2-3 5-3 5S0 5 0 3a3 3 0 0 1 3-3z" fill="#444"/></svg><span>2000 years old. Edwin Larkhall, a Latin professor at</span></li>
      <li><svg width="7" height="7" viewBox="0 0 7 7"><path d="M1 0l2 2-1 1 2 2 1-1 2 2-1 1C3 7 0 4 0 1z" fill="#444"/></svg><span>Phone - 031 447 5820</span></li>
      <li><svg width="8" height="7" viewBox="0 0 8 7"><rect y="2" width="8" height="5" fill="#444"/><rect x="2" width="4" height="2" fill="#444"/></svg><span>Fax - 031 447 5821</span></li>
      <li class="nowrap"><svg width="8" height="6" viewBox="0 0 8 6"><rect x=".5" y=".5" width="7" height="5" fill="none" stroke="#444"/><path d="M.5.5L4 3.5 7.5.5" fill="none" stroke="#444"/></svg><span>E-mail - info@brackwellflows.co.uk</span></li>
    </ul>
  </div>
  <div class="foot-col" style="left:207px"><h4>QUICK LINKS</h4><ul><li>Moving Home</li><li>Our Guarantee</li><li>Charges</li><li>My Bill</li><li>Emergencies</li></ul></div>
  <div class="foot-col" style="left:311px"><h4>CUSTOMERS</h4><ul><li>Business services</li><li>Landlord services</li><li>Estate Agents</li><li>Property Contracts</li></ul></div>
  <div class="foot-col" style="left:409px"><h4>NEW BUILDS</h4><ul><li>Heating and Water Design</li><li>Heating Technology</li><li>Housing Estates</li><li>Single Dwelling Install</li><li>Multi Dwelling Installs</li></ul></div>
  <div class="foot-col" style="left:520px"><h4>YOU LOOKING TO DO?</h4><ul><li>Pay your bil</li><li>I need a landlord certificate</li><li>Book an engineer</li><li>Manage your account</li><li>Need a boiler service</li><li>Set Up a Direct Debit</li></ul></div>
</footer>
<div class="bottom-bar">Copyrights@2016Compny name , All rights Reserved</div>
</body>
</html>
```